Start-up coaching and consulting business needs a new logo.

I need a new logo and business card for my coaching and consulting business, called Venmora Coaching. I chose the name since clarify means: to make (a statement or situation) less confused and more comprehensible, to make clear, shed light on, throw light on, elucidate, illuminate, make plain, make simple, explain, explicate, define, spell out; clear up, sort out, resolve etc. And this is the key to successful coaching. The final design should reflect this process.
My focus is on helping people build their resilience. I would like the logo to appeal to a target audience that includes ordinary people trying to deal with the challenges in their life, as well as be appealing to corporate clients. I am not sure whether to include "and consulting" since I think this may make the card too cluttered.
Business
Venmora Coaching

```html
<!DOCTYPE html>
<html lang="en">
<head>
<meta charset="utf-8">
<title>Venmora Coaching – Business Card</title>
<link href="https://fonts.googleapis.com/css2?family=Cinzel:wght@400;600&family=Arimo:wght@400&display=swap" rel="stylesheet">
<style>
  :root {
    --page-bg: #e4e4e4;
    --card-white: #ffffff;
    --ink-grey: #5a5a5a;
    --accent-green: #a4cc3a;
    --grad-blue: #1a7fd4;
    --grad-teal: #3f9fa0;
    --grad-green: #9ccf58;
    --on-dark: #ffffff;
  }
  * { margin: 0; padding: 0; box-sizing: border-box; }
  html, body {
    width: 1200px; height: 1000px; overflow: hidden;
    background: var(--page-bg);
  }
  .sheet {
    width: 1200px; height: 1000px;
    display: flex; flex-direction: column;
    align-items: center; justify-content: center; gap: 60px;
  }
  .card {
    width: 700px; height: 400px; position: relative;
    box-shadow: 0 6px 18px rgba(0,0,0,.18);
  }
  .card-front {
    background: var(--card-white);
    display: flex; flex-direction: column;
    align-items: center; justify-content: center; gap: 26px;
  }
  .front-dot {
    width: 70px; height: 70px; border-radius: 50%;
    background: var(--accent-green);
  }
  .front-wordmark {
    font-family: "Cinzel", serif; font-weight: 400;
    font-size: 44px; color: var(--ink-grey); letter-spacing: 1px;
  }
  .card-back {
    background: linear-gradient(20deg, var(--grad-blue) 0%, var(--grad-teal) 45%, var(--grad-green) 100%);
    color: var(--on-dark);
  }
  .brand-block {
    position: absolute; left: 40px; top: 42px;
    display: flex; align-items: center; gap: 18px;
  }
  .brand-dot {
    width: 56px; height: 56px; border-radius: 50%;
    background: var(--on-dark);
  }
  .brand-name {
    font-family: "Cinzel", serif; font-weight: 400;
    font-size: 36px; line-height: 1;
  }
  .brand-tagline {
    font-family: "Cinzel", serif; font-weight: 400;
    font-size: 11.5px; letter-spacing: 1.2px; margin-top: 4px;
  }
  .contact {
    position: absolute; right: 44px; top: 168px;
    text-align: right;
  }
  .contact-name {
    font-family: "Cinzel", serif; font-weight: 600; font-size: 24px;
  }
  .contact-credentials,
  .contact-line {
    font-family: "Arimo", Arial, sans-serif; font-size: 17px;
  }
  .contact-credentials { margin-top: 4px; }
  .contact-lines { margin-top: 34px; display: flex; flex-direction: column; gap: 12px; }
</style>
</head>
<body>
  <main class="sheet">
    <section class="card card-front" aria-label="Card front">
      <span class="front-dot"></span>
      <h1 class="front-wordmark">Venmora Coaching</h1>
    </section>

    <section class="card card-back" aria-label="Card back">
      <div class="brand-block">
        <span class="brand-dot"></span>
        <div>
          <p class="brand-name">Venmora Coaching</p>
          <p class="brand-tagline">Personal and Organizational Coaching</p>
        </div>
      </div>
      <div class="contact">
        <p class="contact-name">Maren Kovacs</p>
        <p class="contact-credentials">M.Ed., CTDP, E-RYT-500</p>
        <div class="contact-lines">
          <p class="contact-line">604 555 0142</p>
          <p class="contact-line">778 555 0187</p>
          <p class="contact-line">maren.kovacs@venmoracoaching.com</p>
          <p class="contact-line">www.venmoracoaching.com</p>
        </div>
      </div>
    </section>
  </main>
</body>
</html>
```